Web Page Color Scheme

I need the colors chosen for all of the elements in a B2B web application page (screenshot attached).

We have a web application that serves businesses (not consumers), generally Corvane 300 companies. The pages are fully developed/functional. What I want is to improve the look and feel so that the page has a more premium feel. That is the entire goal, to make the pages have a very premium feel to them. I don’t know if it is the best analogy but if you think of Varn or Pallisene as average and KTR or Osprin as premium, we want users to get a very premium feel the first time they see the screens.

What I am looking for right now is just colors. Below I describe the details.

#1 Improve the colors

The color scheme is blue and yellow. Black, gray and white are also used. I do not think the base colors should change (that is, I think we will continue to use blue and yellow) but I do think which hues, shades, tints or tones of blue, yellow and gray we use could benefit from some improvement. Feel free to use any blues, yellows and grays you think look best, lighter or darker colors, etc. You can also feel free to change what colors are used where. One note, aqua blue does not look premium. It might be deco looking or otherwise good for some things but I don’t think you will see an aqua colored Hollaway driving down the street any time soon.

Quill products tend to have a premium feel but I don’t think I am looking for a stark white appearance.

I want every color defined including but not necessarily limited to:

Backgrounds

Page Header
Navigation Panel
Page Body
Table Header
Table Header Button (the Add button)
Table Column Header
Table Rows (maybe alternating, maybe not)
Checkboxes
Table Footer

Not all of these have to be different. I assume some will be the same. I just need each carefully
thought through.

Fonts

Page Header
Navigation Panel
Page Title
Table Header Title
Table Header Button
Table Column Header
Table Row
Table Footer

Icons

Page Header
Navigation Panel
Table expander/collapse
Actions
Table Footer

Target Market(s)

Corvane 300/Pinnacle 1200

Requirements
Must have
• Premium feel

```html
<!DOCTYPE html>
<html lang="en">
<head>
<meta charset="utf-8">
<title>Veltro Data – Data Sources</title>
<link rel="stylesheet" href="https://fonts.googleapis.com/css2?family=Roboto:wght@400;500;700&display=swap">
<style>
:root{
  --c-header:#3d8fc1;
  --c-nav:#2e343d;
  --c-nav-text:#eceef1;
  --c-body:#e5e6e8;
  --c-panel-head:#c9ced6;
  --c-white:#ffffff;
  --c-row-alt:#f1f1f1;
  --c-line:#d5d8dc;
  --c-text:#1d1f22;
  --c-add:#ffc529;
  --c-active:#5cb85c;
  --c-inactive:#343a40;
  --c-pending:#ffc107;
  --c-bolt:#1a56e0;
  --c-edit:#23963a;
  --c-copy:#f0a800;
  --c-trash:#e53935;
  --c-expander:#2f7fc1;
  --c-page:#1b8fb8;
}
*{box-sizing:border-box;margin:0;padding:0}
html,body{width:1200px;height:1200px;overflow:hidden;background:#fff}
body{font-family:"Roboto",Arial,sans-serif;color:var(--c-text)}
.stage{position:absolute;left:0;top:0;width:1500px;height:1500px;transform:scale(.8);transform-origin:0 0}
.abs{position:absolute}
.app-header{left:308px;top:77px;width:895px;height:63px;background:var(--c-header);color:#fff}
.brand{position:absolute;left:3px;top:21px;display:flex;align-items:center;gap:9px;font-size:19px;font-weight:700}
.brand-mark{width:35px;height:16px;background:#fff;border:1px solid #222}
.menu-toggle{margin-left:4px}
.header-tools{position:absolute;right:28px;top:25px;display:flex;align-items:center;gap:14px;font-size:14px}
.header-tools svg{width:17px;height:17px}
.user{display:flex;align-items:center;gap:6px;margin-left:4px}
.nav{left:308px;top:140px;width:243px;height:1335px;background:var(--c-nav);color:var(--c-nav-text);font-size:15px}
.nav-item{position:absolute;display:flex;align-items:center;gap:9px;white-space:nowrap}
.nav-item svg{width:19px;height:16px}
.content{left:551px;top:140px;width:652px;height:1335px;background:var(--c-body)}
.page-title{left:579px;top:151px;font-size:17px;font-weight:700}
.search{left:1067px;top:151px;width:102px;height:11px;border:1px solid #777;background:#ddd}
.search-icon{left:1171px;top:151px;width:12px;height:12px}
.panel{background:var(--c-white);border:1px solid #c3c6ca}
.panel-head{height:58px;background:var(--c-panel-head);display:flex;align-items:center;padding-left:17px;gap:10px;font-size:15px;border-bottom:1px solid var(--c-line)}
.add-btn{background:var(--c-add);font-size:11px;padding:1px 9px;line-height:12px;border:1px solid #e0a800}
table{border-collapse:collapse;table-layout:fixed;width:100%;font-size:15px}
td,th{height:58px;vertical-align:middle;border-bottom:1px solid var(--c-line)}
th{font-weight:700;background:var(--c-white)}
tr:last-child td{border-bottom:none}
.alt td{background:var(--c-row-alt)}
.sep{border-left:1px solid var(--c-line)}
.c{text-align:center}
.exp{width:18px;height:18px;display:block;margin:0 auto}
.badge{display:inline-block;color:#fff;font-size:14px;padding:2px 0;width:70px;text-align:center;border-radius:3px}
.b-active{background:var(--c-active)}
.b-inactive{background:var(--c-inactive)}
.b-pending{background:var(--c-pending)}
.actions{display:flex;justify-content:space-around;padding:0 4px}
.actions svg,.ico{width:16px;height:16px}
.chk{width:13px;height:13px;border:1px solid #555;display:inline-block;background:#fff}
.chk.on{background:var(--c-trash);border-color:var(--c-trash);position:relative}
.footer{display:flex;align-items:center;padding-left:20px;font-size:15px;height:38px}
.page-size{margin-left:9px;border:1px solid #999;font-size:10px;padding:1px 4px;width:35px}
.pager{position:absolute;left:287px;top:9px;display:flex;align-items:center;gap:8px;color:#666;font-size:13px}
.page-num{background:var(--c-page);color:#fff;width:23px;height:21px;text-align:center;line-height:21px;font-size:14px}
</style>
</head>
<body>
<svg width="0" height="0" style="position:absolute">
  <defs>
    <symbol id="i-bolt" viewBox="0 0 16 16"><path d="M9.5 0 3 9h4l-1.5 7L13 6H8.8z" fill="var(--c-bolt)"/></symbol>
    <symbol id="i-edit" viewBox="0 0 16 16"><path d="M2 3h7v1.6H3.6v8.8h8.8V8H14v7H2z" fill="var(--c-edit)"/><path d="M12.6 1 15 3.4 8.4 10H6V7.6z" fill="var(--c-edit)"/></symbol>
    <symbol id="i-copy" viewBox="0 0 16 16"><path d="M5 1h8v10H5z M2 5h2v9h7v1.5H2z" fill="none" stroke="var(--c-copy)" stroke-width="1.6"/></symbol>
    <symbol id="i-trash" viewBox="0 0 16 16"><path d="M2 3h12M6 3V1.5h4V3M3.5 3.5l1 11h7l1-11M6.5 6v6M9.5 6v6" fill="none" stroke="var(--c-trash)" stroke-width="1.5"/></symbol>
    <symbol id="i-exp" viewBox="0 0 18 18"><circle cx="9" cy="9" r="9" fill="var(--c-expander)"/><path d="M7.5 5 11.5 9l-4 4" fill="none" stroke="#fff" stroke-width="2.2"/></symbol>
  </defs>
</svg>

<div class="stage">
  <header class="abs app-header">
    <div class="brand"><span class="brand-mark"></span>Veltro Data
      <svg class="menu-toggle" width="15" height="13" viewBox="0 0 15 13"><path d="M0 1.5h15M0 6.5h15M0 11.5h15" stroke="#fff" stroke-width="2.2"/></svg>
    </div>
    <div class="header-tools">
      <svg viewBox="0 0 16 16"><path d="M1 12a7 7 0 0 1 14 0z" fill="#fff"/><path d="M8 12 11 6" stroke="var(--c-header)" stroke-width="1.6"/></svg>
      <svg viewBox="0 0 16 16"><path d="M2 14 10 6" stroke="#fff" stroke-width="2.4"/><path d="M12 1v3M10.5 2.5h3M14 7v2M13 8h2M7 1v2M6 2h2" stroke="#fff" stroke-width="1.2"/></svg>
      <svg viewBox="0 0 16 16"><circle cx="8" cy="8" r="7" fill="#fff"/><text x="8" y="12" font-size="11" font-weight="700" text-anchor="middle" fill="var(--c-header)">?</text></svg>
      <svg viewBox="0 0 16 16"><circle cx="8" cy="8" r="5" fill="none" stroke="#fff" stroke-width="3.5" stroke-dasharray="2.6 1.3"/><circle cx="8" cy="8" r="4" fill="#fff"/><circle cx="8" cy="8" r="1.7" fill="var(--c-header)"/></svg>
      <span class="user">Tom Renner <svg width="11" height="7" viewBox="0 0 11 7" style="width:11px;height:7px"><path d="M0 0h11L5.5 7z" fill="#fff"/></svg></span>
    </div>
  </header>

  <nav class="abs nav">
    <div class="nav-item" style="left:24px;top:17px"><svg viewBox="0 0 20 16"><circle cx="6" cy="5" r="3" fill="none" stroke="#ddd" stroke-width="1.3"/><circle cx="14" cy="5" r="3" fill="none" stroke="#ddd" stroke-width="1.3"/><path d="M1 15c0-4 10-4 10 0M9 15c0-4 10-4 10 0" fill="none" stroke="#ddd" stroke-width="1.3"/></svg>Users</div>
    <div class="nav-item" style="left:60px;top:47px">Roles</div>
    <div class="nav-item" style="left:60px;top:72px">Notification Group</div>
    <div class="nav-item" style="left:24px;top:106px"><svg viewBox="0 0 20 16"><ellipse cx="10" cy="3" rx="6" ry="2.2" fill="none" stroke="#ddd" stroke-width="1.3"/><path d="M4 3v10c0 3 12 3 12 0V3M4 8c0 3 12 3 12 0" fill="none" stroke="#ddd" stroke-width="1.3"/></svg>Data Sources</div>
    <div class="nav-item" style="left:60px;top:150px">Data Object Relationship</div>
    <div class="nav-item" style="left:24px;top:196px"><svg viewBox="0 0 20 16"><rect x="2" y="2" width="16" height="12" fill="none" stroke="#ddd" stroke-width="1.3"/><path d="M2 8h16M10 2v12M5 5h3M12 5h3M5 11h3M12 11h3" stroke="#ddd" stroke-width="1.1"/></svg>Data Sets</div>
    <div class="nav-item" style="left:53px;top:242px">Rule Sets</div>
    <div class="nav-item" style="left:24px;top:287px"><svg viewBox="0 0 20 16"><circle cx="10" cy="8" r="7" fill="none" stroke="#ddd" stroke-width="1.3"/><path d="M10 4v4l3 2" fill="none" stroke="#ddd" stroke-width="1.3"/></svg>Schedules</div>
    <div class="nav-item" style="left:24px;top:333px"><svg viewBox="0 0 20 16"><path d="M2 5h13l-3-3M18 11H5l3 3" fill="none" stroke="#ddd" stroke-width="1.4"/><rect x="6" y="6" width="8" height="4" fill="none" stroke="#ddd" stroke-width="1"/></svg>Metadata Import/Export</div>
    <div class="nav-item" style="left:60px;top:365px">Import</div>
    <div class="nav-item" style="left:60px;top:392px">Export</div>
  </nav>

  <main class="abs content"></main>
  <h1 class="abs page-title">Data Sources</h1>
  <div class="abs search"></div>
  <svg class="abs search-icon" viewBox="0 0 12 12"><circle cx="5" cy="5" r="3.6" fill="none" stroke="var(--c-expander)" stroke-width="1.8"/><path d="M7.6 7.6 11 11" stroke="var(--c-expander)" stroke-width="2"/></svg>

  <!-- Data sources panel -->
  <section class="abs panel" style="left:567px;top:187px;width:618px">
    <div class="panel-head">Data Sources <span class="add-btn">Add</span></div>
    <table>
      <colgroup><col style="width:44px"><col style="width:161px"><col style="width:166px"><col style="width:99px"><col></colgroup>
      <tr><th colspan="2" style="text-align:left;padding-left:17px">Data Source Name <svg width="10" height="6" style="margin-left:4px"><path d="M0 6h10L5 0z" fill="#222"/></svg></th><th class="sep c">Type ⇕</th><th class="sep c">Status ⇕</th><th class="sep c">Action</th></tr>
      <tr class="alt"><td><svg class="exp"><use href="#i-exp"/></svg></td><td class="sep" style="padding-left:41px">Basalt DB</td><td class="sep"></td><td class="sep c"><span class="badge b-active">Active</span></td><td class="sep"><div class="actions"><svg><use href="#i-bolt"/></svg><svg><use href="#i-edit"/></svg><svg><use href="#i-copy"/></svg><svg><use href="#i-trash"/></svg></div></td></tr>
      <tr><td><svg class="exp"><use href="#i-exp"/></svg></td><td class="sep" style="padding-left:41px">Basalt DB</td><td class="sep c">Orbitcrm.net</td><td class="sep c"><span class="badge b-active">Active</span></td><td class="sep"><div class="actions"><svg><use href="#i-bolt"/></svg><svg><use href="#i-edit"/></svg><svg><use href="#i-copy"/></svg><svg><use href="#i-trash"/></svg></div></td></tr>
      <tr class="alt"><td><svg class="exp"><use href="#i-exp"/></svg></td><td class="sep" style="padding-left:41px">Basalt DB</td><td class="sep c">Orbitcrm.net</td><td class="sep c"><span class="badge b-inactive">Inactive</span></td><td class="sep"><div class="actions"><svg><use href="#i-bolt"/></svg><svg><use href="#i-edit"/></svg><svg><use href="#i-copy"/></svg><svg><use href="#i-trash"/></svg></div></td></tr>
      <tr><td style="height:50px"><svg class="exp"><use href="#i-exp"/></svg></td><td class="sep" style="padding-left:41px">Basalt DB</td><td class="sep c">Orbitcrm.net</td><td class="sep c"><span class="badge b-pending">Pending</span></td><td class="sep"><div class="actions"><svg><use href="#i-bolt"/></svg><svg><use href="#i-edit"/></svg><svg><use href="#i-copy"/></svg><svg><use href="#i-trash"/></svg></div></td></tr>
    </table>
  </section>

  <!-- Data objects panel -->
  <section class="abs panel" style="left:568px;top:570px;width:616px">
    <div class="panel-head">Data Objects <span class="add-btn">Add</span></div>
    <table>
      <colgroup><col style="width:44px"><col style="width:475px"><col></colgroup>
      <tr><th colspan="2" style="text-align:left;padding-left:34px">Data Object Name</th><th class="sep c">Action</th></tr>
      <tr class="alt"><td><svg class="exp"><use href="#i-exp"/></svg></td><td class="sep" style="padding-left:34px"><span>Account</span><span style="position:absolute;left:390px">28 fields</span></td><td class="sep"><svg class="ico" style="display:block;margin:0 auto"><use href="#i-trash"/></svg></td></tr>
    </table>
  </section>

  <!-- Fields panel -->
  <section class="abs panel" style="left:566px;top:769px;width:618px">
    <div class="panel-head">Fields <span class="add-btn">Add</span></div>
    <table>
      <colgroup><col style="width:129px"><col style="width:149px"><col style="width:102px"><col style="width:88px"><col></colgroup>
      <tr><th style="text-align:left;padding-left:31px">Field Name</th><th class="c">Data Type</th><th class="sep c">Primary Key</th><th class="sep c">Rule Types</th><th class="sep c">Action</th></tr>
      <tr class="alt"><td style="padding-left:31px">Id</td><td class="c">Common Id</td><td class="sep c"><span class="chk on"><svg width="11" height="11" viewBox="0 0 11 11" style="position:absolute;left:0;top:0"><path d="M2 5.5 4.5 8 9 3" fill="none" stroke="#fff" stroke-width="1.8"/></svg></span></td><td class="sep"></td><td class="sep"><div class="actions" style="padding:0 30px"><svg><use href="#i-edit"/></svg><svg><use href="#i-trash"/></svg></div></td></tr>
      <tr><td style="padding-left:31px">Name</td><td class="c">Organization Name</td><td class="sep c"><span class="chk"></span></td><td class="sep"></td><td class="sep"><div class="actions" style="padding:0 30px"><svg><use href="#i-edit"/></svg><svg><use href="#i-trash"/></svg></div></td></tr>
      <tr class="alt"><td style="padding-left:31px">Phone</td><td class="c">Phone Number</td><td class="sep c"><span class="chk"></span></td><td class="sep"></td><td class="sep"><div class="actions" style="padding:0 30px"><svg><use href="#i-edit"/></svg><svg><use href="#i-trash"/></svg></div></td></tr>
      <tr><td style="height:50px;padding-left:31px">Type</td><td class="c">Address</td><td class="sep c"><span class="chk"></span></td><td class="sep"></td><td class="sep"><div class="actions" style="padding:0 30px"><svg><use href="#i-edit"/></svg><svg><use href="#i-trash"/></svg></div></td></tr>
    </table>
  </section>

  <!-- More data objects -->
  <section class="abs panel" style="left:565px;top:1125px;width:619px">
    <table>
      <colgroup><col style="width:52px"><col style="width:494px"><col></colgroup>
      <tr class="alt"><td><svg class="exp"><use href="#i-exp"/></svg></td><td style="padding-left:43px;position:relative">Contact<span style="position:absolute;left:426px">26 fields</span></td><td class="sep"><svg class="ico" style="display:block;margin:0 auto"><use href="#i-trash"/></svg></td></tr>
      <tr><td><svg class="exp"><use href="#i-exp"/></svg></td><td style="padding-left:49px;position:relative">Lead<span style="position:absolute;left:427px">17 fields</span></td><td class="sep"><svg class="ico" style="display:block;margin:0 auto"><use href="#i-trash"/></svg></td></tr>
    </table>
  </section>

  <!-- More data sources -->
  <section class="abs panel" style="left:564px;top:1256px;width:618px">
    <table>
      <colgroup><col style="width:44px"><col style="width:302px"><col style="width:90px"><col></colgroup>
      <tr class="alt"><td><svg class="exp"><use href="#i-exp"/></svg></td><td class="sep" style="padding-left:27px;position:relative">ocrm 99<span style="position:absolute;left:188px">Orbitcrm.net</span></td><td class="sep c"><span class="badge b-active">Active</span></td><td class="sep"><div class="actions"><svg><use href="#i-bolt"/></svg><svg><use href="#i-edit"/></svg><svg><use href="#i-copy"/></svg><svg><use href="#i-trash"/></svg></div></td></tr>
      <tr><td><svg class="exp"><use href="#i-exp"/></svg></td><td class="sep" style="padding-left:13px;position:relative">OCRM field entry test<span style="position:absolute;left:188px">Orbitcrm.net</span></td><td class="sep c"><span class="badge b-active">Active</span></td><td class="sep"><div class="actions"><svg><use href="#i-bolt"/></svg><svg><use href="#i-edit"/></svg><svg><use href="#i-copy"/></svg><svg><use href="#i-trash"/></svg></div></td></tr>
    </table>
  </section>

  <!-- Table footer -->
  <footer class="abs panel footer" style="left:564px;top:1383px;width:618px">
    6 of 6 records <span class="page-size">20 ⌄</span>
    <div class="pager"><span>«</span><span>‹</span><span class="page-num">1</span><span>›</span><span>»</span></div>
  </footer>
</div>
</body>
</html>
```